Steady Harbour Coaching Business Card

We need a business card for a new business based in Sydney Australia called "Steady Harbour Coaching". The business provides the following:
1. Resilience systems for individuals - Developing personalised resilience programs that increase stress tolerance, improve work effectiveness and minimise stress responses to challenge.
2. Group Resilience Training for Leaders and managers - Delivering Resilience training packages and ongoing support to leadership cadres within organisations.
3. High Risk Resilience Training - providing resilience training for High Risk professions such as emergency responders, military and police.

Target Market(s)

Corporate / Military / Emergency Responders

Industry/Entity Type

Leadership

Contact Information for Business Card

Steady Harbour Coaching, Derek Falwood, 7/19 Kestrel St Penbrook 2093, quiet.morning.tide@mailpost.example, www.steadyharbourcoaching.example.au, M# 0417603842
Personalised Mental Resilience Systems for leaders and high risk professions

Requirements
Must have
• 1. Creation of a logo/graphic - to include 3 elements:
a. Military
b.Corporate
c. Emergency Responder.

As long as those 3 elements are included - I am open to any potential designs. Preference given to those who can create a logo out of the above three elements.

```html
<!DOCTYPE html>
<html lang="en">
<head>
<meta charset="utf-8">
<title>Steady Harbour Coaching – Business Card</title>
<link rel="stylesheet" href="https://fonts.googleapis.com/css2?family=Tinos&family=Open+Sans:wght@400;600&display=swap">
<style>
  :root {
    --page: #e8e5e0;
    --paper-light: #ffffff;
    --paper-shade: #d9d9dc;
    --navy: #221c5c;
    --navy-deep: #17123f;
    --stripe: #8a8a8f;
    --charcoal: #2c2c2f;
    --charcoal-deep: #1f1f22;
    --ink-light: #f2f2f4;
    --ink-soft: #d6d6da;
    --figure-tone: #6f6f74;
    --map-tone: #38383c;
  }
  * { box-sizing: border-box; margin: 0; padding: 0; }
  html, body { width: 1200px; height: 1023px; overflow: hidden; background: var(--page); }
  body { display: flex; align-items: center; justify-content: center; }

  .business-card {
    position: relative;
    width: 900px;
    height: 515px;
    border-radius: 26px;
    overflow: hidden;
    background: var(--charcoal);
    box-shadow: 0 14px 40px rgba(0,0,0,.25);
  }
  .card-top {
    position: absolute; left: 0; top: 0; width: 100%; height: 170px;
    background: linear-gradient(180deg, var(--paper-light) 0%, var(--paper-shade) 100%);
  }
  .title-band {
    position: absolute; left: 0; top: 170px; width: 100%; height: 122px;
    background: linear-gradient(180deg, var(--navy) 0%, var(--navy-deep) 100%);
  }
  .accent-stripe {
    position: absolute; left: 0; top: 292px; width: 100%; height: 12px;
    background: var(--stripe);
  }
  .card-bottom {
    position: absolute; left: 0; top: 304px; width: 100%; height: 211px;
    background: linear-gradient(180deg, var(--charcoal) 0%, var(--charcoal-deep) 100%);
  }
  .team-figures {
    position: absolute; left: 60px; top: 70px; width: 230px; height: 270px;
    background: linear-gradient(180deg, var(--figure-tone) 0%, #4e4e53 100%);
    border-radius: 60px 60px 8px 8px;
    opacity: .85;
  }
  .region-map {
    position: absolute; left: 330px; top: 318px; width: 200px; height: 150px;
    background: var(--map-tone);
    border-radius: 40% 50% 45% 55%;
  }
  .business-name {
    position: absolute; right: 56px; top: 182px;
    font-family: "Tinos", "Times New Roman", serif;
    font-size: 46px; line-height: 48px;
    color: var(--ink-light);
    text-align: right;
    text-shadow: 2px 2px 3px rgba(0,0,0,.55);
  }
  .holder-name {
    position: absolute; left: 60px; bottom: 58px;
    font-family: "Open Sans", Arial, sans-serif;
    font-size: 26px; color: var(--ink-light);
  }
  .contact-list {
    position: absolute; right: 46px; top: 326px;
    list-style: none;
    font-family: "Open Sans", Arial, sans-serif;
    font-size: 19px; line-height: 36px;
    color: var(--ink-soft);
    text-align: right;
  }
  .contact-list li { display: flex; align-items: center; justify-content: flex-end; gap: 14px; }
  .contact-icon { width: 16px; height: 16px; fill: none; stroke: var(--ink-soft); stroke-width: 1.6; }
</style>
</head>
<body>
  <div class="business-card">
    <div class="card-top"></div>
    <div class="title-band"></div>
    <div class="accent-stripe"></div>
    <div class="card-bottom"></div>

    <div class="region-map" role="img" aria-label="Faint map of Australia"></div>
    <div class="team-figures" role="img" aria-label="Silhouettes of a soldier, a business person and an emergency responder"></div>

    <h1 class="business-name">Steady Harbour<br>Coaching</h1>
    <p class="holder-name">Derek Falwood</p>

    <ul class="contact-list">
      <li>0417603842
        <svg class="contact-icon" viewBox="0 0 16 16"><rect x="4" y="1" width="8" height="14" rx="1.5"/><line x1="7" y1="12.5" x2="9" y2="12.5"/></svg>
      </li>
      <li>7/19 Kestrel St Penbrook 2093
        <svg class="contact-icon" viewBox="0 0 16 16"><path d="M8 15s5-5.5 5-9a5 5 0 0 0-10 0c0 3.5 5 9 5 9z"/><circle cx="8" cy="6" r="1.8"/></svg>
      </li>
      <li>quiet.morning.tide@mailpost.example
        <svg class="contact-icon" viewBox="0 0 16 16"><rect x="1.5" y="3.5" width="13" height="9"/><path d="M1.5 3.5 8 9l6.5-5.5"/></svg>
      </li>
      <li>www.steadyharbourcoaching.example.au
        <svg class="contact-icon" viewBox="0 0 16 16"><circle cx="8" cy="8" r="6.5"/><ellipse cx="8" cy="8" rx="3" ry="6.5"/><line x1="1.5" y1="8" x2="14.5" y2="8"/></svg>
      </li>
    </ul>
  </div>
</body>
</html>
```